Pelvin Advisory Business Card Design

Business card for business consulting company, using attached logo. We do financial and strategic consulting, and want a clean, professional image with a bit of fun. Our logo is a flat whale tail, which symbolizes the Orca whale, a highly collaborative, group based animal that is very successful in navigating the ocean, protecting the herd, and hunting. We like the logo that is blue and gray on white one one side, but would be open to a blue card with white lettering on the other side... or whatever you'd suggest
Updates
Hi all - I have had the logo modified to take the shadowing off the tail. I will post it on the brief... under a file name called updated logo. thank you Added Saturday, April 25, 2015
Target Market(s)
Small to medium sized businesses ($10M to $500M in revenue per year), financial and sales executives, general managers, attorneys and CPAs
Industry/Entity Type
Financial
Contact Information for Business Card
Want company name, contact info - name, title, telephone, email, website, linkedin, twitter and Facebook. No physical address yet.
Requirements
Must have
- contemporary design, bold, strong, confident but with a bit of fun. prominently feature the logo and the whale tail icon
Nice to have
- unique touches that would differentiate us from a regular card... for example, logo and writing all on front on white background, but on back - logo in white on a blue background
- open to idea of different shapes of card than standard... but not sure

```html
<!DOCTYPE html>
<html lang="en">
<head>
<meta charset="utf-8">
<title>Pelvin Advisory Business Card</title>
<link rel="stylesheet" href="https://fonts.googleapis.com/css2?family=Source+Sans+3:wght@300;400;600&display=swap">
<style>
  :root {
    --navy: #1b3f6e;
    --navy-deep: #14325a;
    --navy-panel: #1a3a64;
    --ink: #2a2a2a;
    --grey: #8a8a8a;
    --paper: #ffffff;
    --stage: #e9e7e3;
  }
  * { box-sizing: border-box; margin: 0; padding: 0; }
  html, body { width: 1200px; height: 902px; overflow: hidden; }
  body {
    background: var(--stage);
    font-family: "Source Sans 3", "Segoe UI", sans-serif;
    display: flex;
    align-items: center;
    justify-content: center;
    gap: 40px;
  }
  .card {
    position: relative;
    width: 540px;
    height: 309px;
    border-radius: 22px;
    overflow: hidden;
    box-shadow: 0 6px 18px rgba(0,0,0,0.18);
  }

  /* Back side */
  .card-back {
    background: linear-gradient(150deg, #1d4677 0%, var(--navy) 45%, var(--navy-deep) 100%);
    display: flex;
    align-items: center;
    justify-content: center;
  }
  .back-badge {
    display: flex;
    align-items: center;
    gap: 12px;
    padding: 26px 30px;
    border-radius: 20px;
    background: var(--navy-panel);
  }
  .back-badge .mark-square {
    width: 22px; height: 22px; background: var(--paper); border-radius: 3px;
  }
  .back-badge .back-name {
    color: var(--paper);
    font-size: 24px;
    font-weight: 400;
  }

  /* Front side */
  .card-front { background: var(--paper); }
  .tab {
    position: absolute;
    background: var(--navy);
    width: 112px;
    height: 26px;
  }
  .tab-top { top: 0; right: 130px; }
  .tab-bottom { bottom: 0; left: 70px; }

  .brand {
    position: absolute;
    top: 78px;
    left: 96px;
    display: flex;
    flex-direction: column;
    align-items: flex-end;
  }
  .brand-row {
    display: flex;
    align-items: center;
    gap: 10px;
  }
  .brand .mark-square {
    width: 30px; height: 30px; background: var(--navy); border-radius: 6px;
  }
  .brand-name {
    font-size: 28px;
    font-weight: 400;
    color: var(--navy);
    line-height: 1;
    white-space: nowrap;
  }
  .brand-tagline {
    margin-top: 3px;
    font-size: 9px;
    font-weight: 300;
    color: var(--grey);
    letter-spacing: 0.3px;
  }

  .social {
    position: absolute;
    top: 54px;
    right: 34px;
    list-style: none;
    font-size: 13px;
    color: var(--ink);
  }
  .social li {
    display: flex;
    align-items: center;
    gap: 6px;
    margin-bottom: 5px;
    white-space: nowrap;
  }
  .social .net-square {
    width: 12px; height: 12px; background: var(--navy); border-radius: 2px;
  }

  .person {
    position: absolute;
    left: 40px;
    top: 196px;
  }
  .person-name {
    font-size: 20px;
    font-weight: 400;
    color: var(--navy);
    letter-spacing: 0.3px;
    white-space: nowrap;
  }
  .person-title {
    font-size: 13px;
    color: var(--grey);
    margin-top: -2px;
  }

  .contact {
    position: absolute;
    left: 178px;
    top: 178px;
    list-style: none;
    font-size: 14px;
    color: var(--ink);
  }
  .contact li {
    display: flex;
    align-items: center;
    gap: 8px;
    margin-bottom: 3px;
    white-space: nowrap;
  }
  .contact svg { width: 12px; height: 12px; fill: #555; }
</style>
</head>
<body>
  <div class="card card-back">
    <div class="back-badge">
      <span class="mark-square"></span>
      <span class="back-name">Pelvin Advisory</span>
    </div>
  </div>

  <div class="card card-front">
    <div class="tab tab-top"></div>
    <div class="tab tab-bottom"></div>

    <div class="brand">
      <div class="brand-row">
        <span class="mark-square"></span>
        <span class="brand-name">Pelvin Advisory</span>
      </div>
      <div class="brand-tagline">business consulting</div>
    </div>

    <ul class="social">
      <li><span class="net-square"></span>/pelvinadvisory</li>
      <li><span class="net-square"></span>@pelvinadvisory</li>
      <li><span class="net-square"></span>/pelvinadvisory</li>
    </ul>

    <div class="person">
      <div class="person-name">YOUR NAME</div>
      <div class="person-title">Title</div>
    </div>

    <ul class="contact">
      <li>
        <svg viewBox="0 0 12 12" aria-hidden="true"><path d="M2.5 1 L4.5 1 L5.2 3.6 L4 4.6 C4.6 6 6 7.4 7.4 8 L8.4 6.8 L11 7.5 L11 9.5 C11 10.3 10.3 11 9.5 11 C5 11 1 7 1 2.5 C1 1.7 1.7 1 2.5 1 Z"/></svg>
        555-014-2380
      </li>
      <li>
        <svg viewBox="0 0 12 12" aria-hidden="true"><path d="M1 3 H11 V10 H1 Z M1.6 3.4 L6 7 L10.4 3.4 Z" fill-rule="evenodd"/></svg>
        info@pelvinadvisory.com
      </li>
      <li>
        <svg viewBox="0 0 12 12" aria-hidden="true"><circle cx="6" cy="6" r="5"/><path d="M1 6 H11 M6 1 C3.5 3.5 3.5 8.5 6 11 M6 1 C8.5 3.5 8.5 8.5 6 11" stroke="#fff" stroke-width="0.8" fill="none"/></svg>
        www.pelvinadvisory.com
      </li>
    </ul>
  </div>
</body>
</html>
```